beauty salon

providing waxing services from a home base this must include which I will provide a price list and an address

Industry/Entity Type

Beauty Salon

Font styles to use
Script

Colors

Designer to choose colors to be used in the design.

```html
<!DOCTYPE html>
<html lang="en">
<head>
<meta charset="utf-8">
<title>Mirela's Garden Salon – Price List</title>
<link rel="stylesheet" href="https://fonts.googleapis.com/css2?family=Lobster&family=Questrial&family=Nunito+Sans:wght@700&family=Oswald:wght@500;700&display=swap">
<style>
  :root{
    --page:#e9e6ea;
    --pink:#d98fd0;
    --pink-soft:#f3dcef;
    --pink-mid:#e6b6e0;
    --plum:#8e2a8f;
    --ink:#2a2a2a;
    --green:#16835f;
    --cream:#f5f0a0;
    --black:#1b1b1b;
    --flower:236,120,170;
  }
  *{box-sizing:border-box;margin:0;padding:0}
  html,body{width:1200px;height:1200px;overflow:hidden;background:var(--page)}
  .flyer{
    position:absolute;left:50px;top:210px;width:1100px;height:780px;
    background:var(--pink);padding:12px;
  }
  .sheet{
    position:relative;width:100%;height:100%;overflow:hidden;
    background:linear-gradient(180deg,#fff 0%,#fff 45%,var(--pink-soft) 80%,var(--pink-mid) 100%);
    font-family:"Questrial",sans-serif;color:var(--ink);
  }
  .flowers-left{position:absolute;left:0;top:0;width:220px;height:200px;
    background:radial-gradient(ellipse 60% 60% at 40% 50%,rgba(var(--flower),.55) 0%,rgba(var(--flower),.3) 55%,rgba(var(--flower),0) 100%)}
  .flowers-top{position:absolute;left:410px;top:8px;width:140px;height:80px;
    background:radial-gradient(ellipse 50% 50% at 50% 50%,rgba(var(--flower),.5) 0%,rgba(var(--flower),.25) 60%,rgba(var(--flower),0) 100%)}
  .photo-legs{position:absolute;right:0;top:0;width:390px;height:235px;
    background:linear-gradient(160deg,#fbeee8 0%,#f1cfc2 55%,#bfe3f0 100%)}
  .brand{position:absolute;left:240px;top:92px;display:flex;align-items:center;gap:12px}
  .brand-dot{width:26px;height:26px;border-radius:50%;background:var(--green)}
  .brand-name{font-family:"Nunito Sans",sans-serif;font-weight:700;font-size:34px;color:var(--plum)}
  .menu{position:absolute}
  .menu h2{font-family:"Lobster",cursive;font-weight:400;font-size:30px;color:var(--plum);margin-bottom:8px}
  .menu ul{list-style:none}
  .menu li{display:flex;align-items:baseline;font-size:21px;line-height:31px}
  .menu li .lead{flex:1;border-bottom:2px dotted var(--ink);margin:0 3px 6px}
  .menu-lady{left:58px;top:222px;width:270px}
  .menu-men{left:370px;top:175px;width:270px}
  .menu-eye{left:370px;top:478px;width:270px}
  .therapist{position:absolute;left:690px;top:248px;width:390px;text-align:center}
  .therapist .role{font-size:24px;color:var(--black)}
  .therapist .name{font-family:"Lobster",cursive;font-size:54px;color:var(--plum);line-height:1.1}
  .therapist .cred{font-size:20px;line-height:1.2}
  .therapist .phone{font-family:"Nunito Sans",sans-serif;font-weight:700;font-size:38px;color:var(--plum);margin-top:22px}
  .therapist .addr{font-size:16px;margin-top:2px}
  .strip{position:absolute;left:690px;top:508px;width:386px;height:38px;background:var(--black);
    border-radius:18px 0 0 0;color:#fff;font-family:"Lobster",cursive;font-size:24px;
    display:flex;align-items:center;justify-content:center;white-space:nowrap}
  .hours{position:absolute;left:650px;top:546px;right:0;height:186px;background:var(--green);
    display:flex;align-items:center;gap:18px;padding-left:34px;color:#fff}
  .now-open{font-family:"Oswald",sans-serif;font-weight:700;font-size:30px;line-height:1;
    writing-mode:vertical-rl;transform:rotate(180deg);text-align:center}
  .hours ul{list-style:none;font-size:23px;line-height:1.35}
  .coupon{position:absolute;left:376px;top:600px;width:274px;height:132px;background:var(--green);
    padding:10px}
  .coupon-inner{width:100%;height:100%;border:2px dashed var(--cream);
    display:flex;flex-direction:column;align-items:center;justify-content:center;gap:4px;
    font-family:"Oswald",sans-serif;color:var(--cream);text-transform:uppercase;white-space:nowrap}
  .coupon .big{font-size:36px;font-weight:700;line-height:1}
  .coupon .small{font-size:20px;font-weight:500;color:#fff;line-height:1}
</style>
</head>
<body>
<div class="flyer">
  <div class="sheet">
    <div class="flowers-left" role="img" aria-label="Pink gerbera daisies"></div>
    <div class="flowers-top" role="img" aria-label="Two small pink gerbera daisies"></div>
    <div class="photo-legs" role="img" aria-label="Photo of smooth legs resting on a blue towel"></div>

    <div class="brand">
      <span class="brand-dot"></span>
      <span class="brand-name">Mirela's Garden Salon</span>
    </div>

    <section class="menu menu-lady">
      <h2>Lady's Waxing</h2>
      <ul>
        <li>Eyebrow<span class="lead"></span>$8</li>
        <li>Upper Lip<span class="lead"></span>$8</li>
        <li>Chin<span class="lead"></span>$8</li>
        <li>Face Wax<span class="lead"></span>$25</li>
        <li>Bikini Line<span class="lead"></span>$15</li>
        <li>G String<span class="lead"></span>$20</li>
        <li>½ Brazilian<span class="lead"></span>$30</li>
        <li>Full Brazilian<span class="lead"></span>$40</li>
        <li>Half Arm<span class="lead"></span>$20</li>
        <li>Upper half Arm<span class="lead"></span>$20</li>
        <li>Full Arm<span class="lead"></span>$25</li>
        <li>Half Leg<span class="lead"></span>$15</li>
        <li>Upper Leg<span class="lead"></span>$20</li>
        <li>¾ Leg<span class="lead"></span>$25</li>
        <li>Full Leg<span class="lead"></span>$35</li>
      </ul>
    </section>

    <section class="menu menu-men">
      <h2>Men's Waxing</h2>
      <ul>
        <li>Eyebrow<span class="lead"></span>$10</li>
        <li>Half arm<span class="lead"></span>$20</li>
        <li>Upper half arm<span class="lead"></span>$25</li>
        <li>Full arm<span class="lead"></span>$30</li>
        <li>Half leg<span class="lead"></span>$25</li>
        <li>Full leg<span class="lead"></span>$45</li>
        <li>Chest wax<span class="lead"></span>$40</li>
        <li>Back wax<span class="lead"></span>$35</li>
      </ul>
    </section>

    <section class="menu menu-eye">
      <h2>Eye Enhancement</h2>
      <ul>
        <li>Eyebrow tint<span class="lead"></span>$12</li>
        <li>Eyelash tint<span class="lead"></span>$15</li>
      </ul>
    </section>

    <section class="therapist">
      <p class="role">Beauty Therapist:</p>
      <p class="name">Mirela</p>
      <p class="cred">Diploma of Beauty Therapy<br>at Hartwell College</p>
      <p class="phone">0400 555 127</p>
      <p class="addr">12 Finch Lane | Hollow Creek</p>
    </section>

    <div class="strip">Waxing Services at Your Door</div>

    <div class="hours">
      <span class="now-open">NOW<br>OPEN</span>
      <ul>
        <li>Wednesday 10am - 4pm</li>
        <li>Fridays 10am-7pm</li>
        <li>Saturday 10am -4pm</li>
      </ul>
    </div>

    <div class="coupon">
      <div class="coupon-inner">
        <span class="big">10% Discount</span>
        <span class="small">On First Treatment</span>
      </div>
    </div>
  </div>
</div>
</body>
</html>
```